Lanternfield Voyages Business Card Design for Home Based Travel Agency

We already have a logo and I would like to see about getting a Business Card Design. The font on the logo can be changed. We are a home based travel agency and sell cruises and tour packages, etc. I would like the following information put into the design Name of Company and Tag Line from the logo. I would also like the email info@lanternfieldvoyages.example Phone 555-238-6140. Website www.lanternfieldvoyages.example. My name Neil Parton Travel Consultant and my wife's Name Mavis Parton. I would like you to use your imagination as nothing is off limites. Impress Me!

Target Market(s)

Baby Boomers

Industry/Entity Type

Travel Agent

Contact Information for Business Card

See above

Font styles to use
Serif
Sans Serif

Colors

Designer to choose colors to be used in the design.

Requirements
Must have
• Play with different fonts and needs to be easily readable, i.e. not too small of print.
Nice to have
• Use your imagination

```html
<!DOCTYPE html>
<html lang="en">
<head>
<meta charset="utf-8">
<title>Lanternfield Voyages – Business Card</title>
<link href="https://fonts.googleapis.com/css2?family=Roboto:wght@400;500;700&family=Roboto+Condensed:wght@700&display=swap" rel="stylesheet">
<style>
  :root {
    --backdrop: #2a2a2a;
    --card: #414141;
    --ink: #ffffff;
    --accent: #2a7fc4;
    --accent-deep: #1560b0;
    --rule: #9a9a9a;
    --band-grey: #8c8c8c;
  }
  * { margin: 0; padding: 0; box-sizing: border-box; }
  html, body { width: 1200px; height: 960px; overflow: hidden; }
  body {
    background: var(--backdrop);
    font-family: "Roboto", Arial, sans-serif;
    color: var(--ink);
    position: relative;
  }
  .card {
    position: absolute;
    width: 600px;
    height: 343px;
    background: var(--card);
    overflow: hidden;
  }
  .card--front { left: 314px; top: 113px; }
  .card--back  { left: 311px; top: 472px; }

  .brand {
    position: absolute;
    display: flex;
    align-items: center;
    gap: 12px;
  }
  .brand__name {
    font-family: "Roboto", Arial, sans-serif;
    font-weight: 400;
    color: var(--ink);
    letter-spacing: 1px;
  }
  .brand__square { background: var(--accent); flex: none; }

  .card--front .brand { right: 36px; top: 150px; }
  .card--front .brand__name { font-size: 28px; }
  .card--front .brand__square { width: 22px; height: 22px; }

  .person { position: absolute; left: 35px; top: 195px; }
  .person__name {
    font-family: "Roboto Condensed", Arial, sans-serif;
    font-weight: 700;
    font-size: 21px;
    color: var(--accent);
    text-transform: uppercase;
    line-height: 24px;
  }
  .person__role {
    font-size: 15px;
    font-weight: 500;
    text-transform: uppercase;
    letter-spacing: 0.3px;
    margin-top: 2px;
  }
  .divider {
    position: absolute;
    left: 35px; top: 246px;
    width: 530px; height: 1px;
    background: var(--rule);
  }
  .contacts { position: absolute; left: 35px; top: 257px; list-style: none; }
  .contacts li {
    display: flex; align-items: center; gap: 7px;
    font-size: 14px; line-height: 19px;
  }
  .contacts svg { width: 13px; height: 13px; flex: none; }

  .band { position: absolute; left: 0; bottom: 0; width: 600px; height: 9px; }
  .band__blue {
    position: absolute; left: 0; top: 0; width: 394px; height: 9px;
    background: linear-gradient(to right, var(--accent-deep), var(--accent));
  }
  .band__grey {
    position: absolute; left: 394px; top: 0; width: 206px; height: 9px;
    background: var(--band-grey);
  }

  .card--back .brand {
    left: 0; right: 0; top: 145px; justify-content: center;
  }
  .card--back .brand__name { font-size: 34px; }
  .card--back .brand__square { width: 28px; height: 28px; }
  .web-line {
    position: absolute; left: 0; right: 0; top: 292px;
    text-align: center; font-size: 14px; letter-spacing: 3px;
  }
</style>
</head>
<body>

<section class="card card--front">
  <div class="brand">
    <span class="brand__square"></span>
    <span class="brand__name">Lanternfield Voyages</span>
  </div>

  <div class="person">
    <p class="person__name">Neil Parton</p>
    <p class="person__role">Travel Consultant</p>
  </div>

  <div class="divider"></div>

  <ul class="contacts">
    <li>
      <svg viewBox="0 0 16 16" aria-hidden="true"><path fill="#2a7fc4" d="M3.6 1.2l2.3 2.6-1.3 1.9c.9 2 2.5 3.6 4.6 4.6l1.9-1.3 2.6 2.3-1.4 2.4C7 13.5 2.5 9 1.3 2.6z"/></svg>
      <span>555-238-6140</span>
    </li>
    <li>
      <svg viewBox="0 0 16 16" aria-hidden="true"><rect x="1" y="3" width="14" height="10" fill="#2a7fc4"/><path d="M1 3.5l7 5 7-5" fill="none" stroke="#414141" stroke-width="1.2"/></svg>
      <span>info@lanternfieldvoyages.example</span>
    </li>
    <li>
      <svg viewBox="0 0 16 16" aria-hidden="true"><circle cx="8" cy="8" r="7" fill="#2a7fc4"/><path d="M1 8h14M8 1c-3 3.5-3 10.5 0 14M8 1c3 3.5 3 10.5 0 14" fill="none" stroke="#414141" stroke-width="1"/></svg>
      <span>www.lanternfieldvoyages.example</span>
    </li>
  </ul>

  <div class="band">
    <span class="band__blue"></span>
    <span class="band__grey"></span>
  </div>
</section>

<section class="card card--back">
  <div class="brand">
    <span class="brand__square"></span>
    <span class="brand__name">Lanternfield Voyages</span>
  </div>
  <p class="web-line">www.lanternfieldvoyages.example</p>
</section>

</body>
</html>
```